NEW site with a tech flair and a feeling of moving forward!!

Hello Everyone,

We are starting with a small project to get the first 3-4 pages done. The winning designer will have an opportunity to work with us to design out the rest of the site. We estimate there will be between 15 and 20 total pages for the site (so there would probably be more work for the winner)!

We need a new website design to enhance the "coolness" factor of our brand image! Our current website is www.quillanmailworks.com and it needs some updating!

We envision a website where the homepage would be almost a landing page. It might have a 60 second video at the top, or a picture slider and contact info/site map at the bottom. In the middle we envision having the 3 service logos along with a quick summary of each service!

We have 3 main services: Tally Up, Shape Up and Send Off. We want to replace those names with our new service names which are: qUrgent, qPromoNet and qBlend-Up. Each service has its own unique logo! :)

If you look at www.quillanmailworks.com and notice the Tally Up / Shape Up / Send Off - - basically we are replacing those names with qUrgent / qPromoNet / and qBlend-Up. Then we just want to freshen things up - for example, the current information listed under "Tally Up" is "good" ...it just doesn't look "cool" ... we need a better way to display it. We provide complex services (and a lot of different services) and are hoping to make a new website that has a feel of being clean, modern, professional, with a technology flair and easy to use/understand our services.

The person visiting the website could watch the 60 second video to get an overview and then click on a logo for their desired service to be able to learn more. Once the user clicks a logo for the desired service, a new page would open and the user could then learn about the service.

After submitting a design for the homepage, please work on a design to totally revamp the "Tally Up" page. We don't like the way that is laid out and need to freshen it up. Note: the layout we choose for Tally Up will be similar for Send Off and Shape Up.

The perfect website will have a combo of a technology flair, a feeling of moving forward and/or of connecting people/things/information together. The website should convey trust.

ABOUT QUILLAN MAILWORKS

We are a technology and communications company. We receive data files, print, fold, insert and mail invoices, statements and other important notices. We also deliver via email, SMS/Text Message and IVR Phone calls. Finally we offer an online website where customers can go to pay their invoices. It is important that the website have a clean, modern, professional and technology look/feel.

We also provide marketing and advertising services through the mail and digitally.

**Please note, our main company is called Quillan Mailworks...we have uploaded our 2 new logos (for your reference) for qUrgent and qPromoNet for reference.

Please message me with any questions! Thanks everyone, looking forward to seeing the designs!

Target Market(s)

Financial companies, Healthcare and Utilities.

Industry/Entity Type

Tech

Number of Pages Required

5+ page

Requirements
Must have
• The perfect website will have a combo of a technology flair, a feeling of moving forward and/or of connecting people/things/information together. The website should convey trust.
Nice to have
• Taking our complicated services and products and making them really simple and easy to understand by using graphs, charts, pictures and other illustrations.
• Eye catchy feel. Needs to be simple. Conveys trustworthy feel.
Should not have
• Can't be boring and bland. Can't be too complex.

```html
<!DOCTYPE html>
<html lang="en">
<head>
<meta charset="utf-8">
<title>Quillan Mailworks</title>
<link rel="stylesheet" href="https://fonts.googleapis.com/css2?family=Raleway:wght@400;500;600;700&family=Open+Sans:wght@400;600;700&display=swap">
<style>
:root{
  --blue:#1592d1;
  --navy:#0b5aa6;
  --deep:#0d4f9a;
  --text:#666;
  --dark:#333;
  --grey:#eeeeee;
  --white:#fff;
}
*{box-sizing:border-box;margin:0;padding:0}
html,body{width:1200px;height:3220px;overflow:hidden}
body{font-family:"Open Sans",Arial,sans-serif;color:var(--text);background:var(--white);position:relative}
a{color:inherit;text-decoration:none}
.topbar{position:absolute;top:0;left:0;width:1200px;height:43px;background:var(--blue);color:var(--white);font-size:16px}
.topbar .mail{position:absolute;left:77px;top:11px;display:flex;align-items:center;gap:10px}
.topbar .links{position:absolute;right:82px;top:11px;display:flex;gap:36px}
.topbar .links .pay{color:#bfe6ff}
.header{position:absolute;top:43px;left:0;width:1200px;height:103px;background:var(--white)}
.brand{position:absolute;left:78px;top:28px;display:flex;align-items:center;gap:12px;font-family:"Raleway",sans-serif;font-size:34px;font-weight:500;color:var(--navy)}
.brand .dot{width:26px;height:26px;border-radius:50%;background:var(--blue)}
.callus{position:absolute;left:503px;top:32px;font-family:"Raleway",sans-serif;font-size:28px;font-weight:600;color:var(--blue)}
.callus span{color:var(--navy);font-weight:500}
.search{position:absolute;left:830px;top:28px;width:292px;height:44px;border:1px solid #ccc;font-size:15px;color:#555;padding:12px 14px}
.search svg{position:absolute;right:12px;top:11px}
.nav{position:absolute;top:146px;left:0;width:1200px;height:62px;background:var(--blue);display:flex;padding-left:77px}
.nav a{color:var(--white);font-size:17px;font-weight:600;line-height:62px;padding:0 29px}
.nav a.active{background:var(--navy)}
.hero{position:absolute;top:208px;left:0;width:1200px;height:470px;background:linear-gradient(180deg,#c9d8e4 0%,#e6edf2 55%,#8f9aa3 100%)}
.hero-copy{position:absolute;right:82px;top:85px;width:620px;text-align:right}
.hero-copy h1{font-family:"Raleway",sans-serif;font-size:70px;font-weight:700;color:var(--navy);line-height:1}
.hero-copy p{font-size:16px;color:#111;margin-top:14px;line-height:1.5}
.btn{display:inline-block;background:var(--navy);color:var(--white);font-family:"Raleway",sans-serif;font-size:21px;border-radius:5px;padding:14px 24px}
.hero-copy .btn{margin-top:16px}
.services{position:absolute;top:678px;left:0;width:1200px;height:312px;display:flex}
.service{flex:1;background:var(--blue);color:var(--white);text-align:center;padding-top:52px}
.service.alt{background:var(--navy)}
.service h2{font-family:"Raleway",sans-serif;font-size:40px;font-weight:500;height:58px}
.service p{font-size:14.5px;line-height:1.85;width:340px;margin:14px auto 0}
.service .play{margin-top:14px}
.about{position:absolute;top:990px;left:0;width:1200px;height:448px}
.about h2{position:absolute;left:80px;top:60px;font-family:"Raleway",sans-serif;font-size:44px;font-weight:500;color:var(--blue)}
.about .body{position:absolute;left:80px;top:122px;width:590px;font-size:14.5px;line-height:1.9}
.about .body p+p{margin-top:10px}
.about .btn{position:absolute;left:78px;top:323px;padding:13px 24px}
.video{position:absolute;left:702px;top:70px;width:421px;height:314px;background:#111}
.video .screen{position:absolute;left:7px;top:7px;width:407px;height:285px;background:linear-gradient(180deg,#a8c5d8,#dbe6ee 60%,#b48a5e)}
.video .bar{position:absolute;left:10px;top:296px;width:400px;height:14px}
.testimonial{position:absolute;top:1438px;left:0;width:1200px;height:447px;background:linear-gradient(135deg,#2f6db6,#3c82c9 50%,#2a65ad);color:var(--white);text-align:center}
.testimonial h2{font-family:"Raleway",sans-serif;font-size:42px;font-weight:400;padding-top:58px}
.testimonial .quote-badge{margin:22px auto 0}
.testimonial blockquote{width:910px;margin:18px auto 0;font-size:14.5px;line-height:1.95}
.client{position:absolute;left:492px;top:352px;display:flex;align-items:center;gap:14px;text-align:left}
.client .avatar{width:70px;height:70px;border-radius:50%;background:#e8eef4;border:3px solid var(--white)}
.client b{font-family:"Raleway",sans-serif;font-size:18px;display:block}
.client small{font-size:13.5px;color:#cfe2f5}
.arrow-l{position:absolute;left:440px;top:378px}
.arrow-r{position:absolute;left:742px;top:378px}
.updates{position:absolute;top:1885px;left:0;width:1200px;height:438px;background:var(--grey)}
.updates h2{text-align:center;font-family:"Raleway",sans-serif;font-size:42px;font-weight:500;color:var(--blue);padding-top:50px}
.card{position:absolute;top:127px;width:509px;height:249px;background:var(--white);display:flex}
.card .photo{width:219px;height:249px}
.card .info{padding:30px 20px 0 20px;width:290px}
.card h3{font-family:"Raleway",sans-serif;font-size:20px;font-weight:700;color:var(--blue)}
.card p{font-size:14px;line-height:1.9;margin-top:12px}
.card .more{display:block;margin-top:6px;font-size:13px;font-weight:700;font-style:italic;color:var(--blue)}
.contact{position:absolute;top:2323px;left:0;width:1200px;height:507px;text-align:center}
.contact h2{font-family:"Raleway",sans-serif;font-size:44px;font-weight:500;color:var(--blue);padding-top:59px}
.contact .lead{width:820px;margin:14px auto 0;font-size:14px;line-height:1.9}
.field{position:absolute;height:50px;border:1px solid #ccc;font-size:14px;color:#555;text-align:left;padding:14px 16px}
.contact .btn{position:absolute;left:515px;top:385px;width:168px;padding:16px 0;font-size:21px}
.footer{position:absolute;top:2830px;left:0;width:1200px;height:326px;background:var(--deep);color:var(--white)}
.footer h4{font-family:"Raleway",sans-serif;font-size:18px;font-weight:700;margin-bottom:18px}
.col{position:absolute;top:32px}
.sitemap li{list-style:none;font-size:14px;line-height:28.5px}
.news-item{display:flex;gap:10px;margin-bottom:14px}
.news-item .thumb{width:66px;height:66px;background:linear-gradient(135deg,#9fd0ec,#e2f1fa);border:2px solid #fff}
.news-item p{font-size:14px;line-height:1.4}
.news-item time{display:block;color:var(--blue);font-size:13.5px}
.touch-row{display:flex;gap:14px;font-size:14px;line-height:1.45;margin-bottom:14px}
.touch-row .hl{color:var(--blue)}
.foot-brand{position:absolute;left:880px;top:110px;width:242px;text-align:center;font-family:"Raleway",sans-serif;font-size:30px;font-weight:500;color:var(--white);padding-bottom:16px;border-bottom:1px solid rgba(255,255,255,.3)}
.social{position:absolute;left:913px;top:188px;display:flex;gap:10px}
.social span{width:48px;height:48px;border-radius:50%;background:var(--blue)}
.copyright{position:absolute;top:3156px;left:0;width:1200px;height:64px;background:var(--blue);color:var(--white);text-align:center;font-size:15px;line-height:64px}
.copyright b{font-weight:700}
</style>
</head>
<body>

<div class="topbar">
  <div class="mail">
    <svg width="20" height="14" viewBox="0 0 20 14"><rect x="1" y="1" width="18" height="12" fill="none" stroke="#fff" stroke-width="1.6"/><path d="M1 1l9 7 9-7" fill="none" stroke="#fff" stroke-width="1.6"/></svg>
    customerservice@quillanmailworks.com
  </div>
  <div class="links"><a class="pay">PayBills</a><a>Careers</a><a>About Us</a><a>Contact Us</a></div>
</div>

<header class="header">
  <div class="brand"><span class="dot"></span>Quillan Mailworks</div>
  <div class="callus">Call us on : <span>555.014.2290</span></div>
  <div class="search">Search...
    <svg width="22" height="22" viewBox="0 0 22 22"><circle cx="9" cy="9" r="6.5" fill="none" stroke="#0b5aa6" stroke-width="2.6"/><path d="M14 14l6 6" stroke="#0b5aa6" stroke-width="3"/></svg>
  </div>
</header>

<nav class="nav">
  <a class="active">HOME</a><a>Q-URGENT</a><a>Q-PROMONET</a><a>QBLEND-UP</a><a>SECURITY</a><a>INDUSTRIES</a>
</nav>

<section class="hero" role="img" aria-label="Photo of a laptop and coffee mug on a desk before a window with a city skyline">
  <div class="hero-copy">
    <h1>Quillan Mailworks</h1>
    <p>We are a technology and communications company. We receive data files, print, fold, insert and mail invoices, statements and other important notices.</p>
    <a class="btn">CONTACT US</a>
  </div>
</section>

<section class="services">
  <div class="service">
    <h2>qUrgent</h2>
    <p>Lorem Ipsum is simply dummy text of the printing and typesetting industry. Lorem Ipsum has been the industry's standard dummy ever since the 1500s, when an unknown</p>
    <svg class="play" width="44" height="44" viewBox="0 0 44 44"><circle cx="22" cy="22" r="20" fill="none" stroke="#fff" stroke-width="2"/><path d="M17 13l13 9-13 9z" fill="#fff"/></svg>
  </div>
  <div class="service alt">
    <h2>qPromoNet</h2>
    <p>Lorem Ipsum is simply dummy text of the printing and typesetting industry. Lorem Ipsum has been the industry's standard dummy ever since the 1500s, when an unknown</p>
    <svg class="play" width="44" height="44" viewBox="0 0 44 44"><circle cx="22" cy="22" r="20" fill="none" stroke="#fff" stroke-width="2"/><path d="M17 13l13 9-13 9z" fill="#fff"/></svg>
  </div>
  <div class="service">
    <h2>qBlend-Up</h2>
    <p>Lorem Ipsum is simply dummy text of the printing and typesetting industry. Lorem Ipsum has been the industry's standard dummy ever since the 1500s, when an unknown</p>
    <svg class="play" width="44" height="44" viewBox="0 0 44 44"><circle cx="22" cy="22" r="20" fill="none" stroke="#fff" stroke-width="2"/><path d="M17 13l13 9-13 9z" fill="#fff"/></svg>
  </div>
</section>

<section class="about">
  <h2>About Us</h2>
  <div class="body">
    <p>At Quillan we are known as an industry leader who brings forward thinking solutions to our customers. Our services save people money, and solve their problems. We bring a high level of customer service, communication and reliability, and provide consistent value to our clients over the long term, providing innovative, technologically-based, confidential solutions to our clients who need them.</p>
    <p>Vision and Mission statements come and go but our values live on. We start with the timeless value of Integrity. It affects everything we do and stand for.</p>
  </div>
  <a class="btn">KNOW MORE</a>
  <div class="video">
    <div class="screen" role="img" aria-label="Video still of a businessman standing before a city skyline"></div>
    <svg class="bar" viewBox="0 0 400 14" width="400" height="14">
      <rect x="2" y="2" width="3" height="10" fill="#fff"/><rect x="8" y="2" width="3" height="10" fill="#fff"/>
      <rect x="20" y="5" width="320" height="4" fill="#444"/><circle cx="26" cy="7" r="3" fill="#fff"/>
      <path d="M352 5h3l4-3v10l-4-3h-3z" fill="#fff"/><rect x="362" y="5" width="16" height="4" fill="#888"/>
      <rect x="386" y="2" width="10" height="10" fill="none" stroke="#fff" stroke-width="1.5"/>
    </svg>
  </div>
</section>

<section class="testimonial" role="group" aria-label="Client testimonial over a faint world map and portraits backdrop">
  <h2>What Our Client Say</h2>
  <svg class="quote-badge" width="70" height="70" viewBox="0 0 70 70"><circle cx="35" cy="35" r="32" fill="none" stroke="#fff" stroke-width="3"/><path d="M22 42c0-9 4-15 10-17v4c-3 2-5 5-5 7h5v10h-10zM38 42c0-9 4-15 10-17v4c-3 2-5 5-5 7h5v10h-10z" fill="#fff"/></svg>
  <blockquote>“Our firm counts on Quillan to mail our quarterly Market Letters, annual reports and other communication that is critical to our client service and growth strategy. Over the years we have relied on their prompt, professional service as well as their creative problem solving. Reaching out to our clients and other stakeholders is an efficient”</blockquote>
  <svg class="arrow-l" width="16" height="26" viewBox="0 0 16 26"><path d="M13 2L3 13l10 11" fill="none" stroke="#cfe2f5" stroke-width="2.5"/></svg>
  <div class="client">
    <div class="avatar" role="img" aria-label="Client portrait"></div>
    <div><b>– Dana Whitcombe</b><small>Senior Vice President</small></div>
  </div>
  <svg class="arrow-r" width="16" height="26" viewBox="0 0 16 26"><path d="M3 2l10 11L3 24" fill="none" stroke="#cfe2f5" stroke-width="2.5"/></svg>
</section>

<section class="updates">
  <h2>Latest Update</h2>
  <article class="card" style="left:77px">
    <div class="photo" role="img" aria-label="Photo of visitors at an aquarium tank" style="background:linear-gradient(160deg,#3d8a8c,#1f5b5e 60%,#6a8a58)"></div>
    <div class="info">
      <h3>Harbor Bay Aquarium</h3>
      <p>The Harbor Bay Aquarium is a private, not -for-profit aquatic and marine science educa- tional facility offering a fun &amp; interesting</p>
      <a class="more">READ MORE… »</a>
    </div>
  </article>
  <article class="card" style="left:612px">
    <div class="photo" role="img" aria-label="Photo of a municipal public works building with stairs" style="background:linear-gradient(180deg,#bcd3e6 0%,#c9b89c 55%,#8d8a84 100%)"></div>
    <div class="info">
      <h3>Leading City</h3>
      <p>The Public Works Department of this leading City provides essential municipal services for the community This includes.</p>
      <a class="more">READ MORE… »</a>
    </div>
  </article>
</section>

<section class="contact">
  <h2>Contact Us</h2>
  <p class="lead">Lorem Ipsum is simply dummy text of the printing and typesetting industry. Lorem Ipsum has been the industry's standard dummy text when an unknown printer took a galley of type and .</p>
  <div class="field" style="left:152px;top:197px;width:292px">Name*</div>
  <div class="field" style="left:454px;top:197px;width:292px">Email*</div>
  <div class="field" style="left:751px;top:197px;width:292px">Phone*</div>
  <div class="field" style="left:152px;top:257px;width:891px;height:112px">Message*</div>
  <a class="btn">SUBMIT</a>
</section>

<footer class="footer">
  <div class="col" style="left:79px">
    <h4>SiteMap</h4>
    <ul class="sitemap"><li>Home</li><li>About</li><li>Services</li><li>Security</li><li>Industries</li><li>PayBill</li><li>Careers</li><li>Contact Us</li></ul>
  </div>
  <div class="col" style="left:344px">
    <h4>Latest News</h4>
    <div class="news-item"><div class="thumb" role="img" aria-label="News thumbnail"></div><p>Do your vendors put you<br>at risk? -Quillan Mailworks<time>February 28,2016</time></p></div>
    <div class="news-item"><div class="thumb" role="img" aria-label="News thumbnail"></div><p>Do your vendors put you<br>at risk? -Quillan Mailworks<time>February 28,2016</time></p></div>
    <div class="news-item"><div class="thumb" role="img" aria-label="News thumbnail"></div><p>Do your vendors put you<br>at risk? -Quillan Mailworks<time>February 28,2016</time></p></div>
  </div>
  <div class="col" style="left:610px">
    <h4>Get In Touch</h4>
    <div class="touch-row">
      <svg width="20" height="26" viewBox="0 0 20 26"><path d="M10 24C4 16 2 12 2 9a8 8 0 0116 0c0 3-2 7-8 15z" fill="none" stroke="#fff" stroke-width="1.6"/><circle cx="10" cy="9" r="3" fill="none" stroke="#fff" stroke-width="1.6"/></svg>
      <div><span class="hl">Quillan Mailworks</span><br>Quillan Mailworks, Inc.<br>1420 NW Alder Ave<br>Riverton, OR 97000</div>
    </div>
    <div class="touch-row">
      <svg width="20" height="20" viewBox="0 0 20 20"><path d="M4 2l4 4-2 3c1 2 3 4 5 5l3-2 4 4-3 3C8 19 1 12 1 5z" fill="none" stroke="#fff" stroke-width="1.6"/></svg>
      <div>555.014.7230 or 855-014-7230</div>
    </div>
    <div class="touch-row">
      <svg width="20" height="20" viewBox="0 0 20 20"><rect x="5" y="2" width="10" height="5" fill="none" stroke="#fff" stroke-width="1.6"/><rect x="2" y="7" width="16" height="7" fill="none" stroke="#fff" stroke-width="1.6"/><rect x="5" y="12" width="10" height="6" fill="none" stroke="#fff" stroke-width="1.6"/></svg>
      <div>555.014.2290</div>
    </div>
    <div class="touch-row">
      <svg width="20" height="16" viewBox="0 0 20 16"><rect x="1" y="1" width="18" height="14" fill="none" stroke="#fff" stroke-width="1.6"/><path d="M1 1l9 7 9-7" fill="none" stroke="#fff" stroke-width="1.6"/></svg>
      <div>customerservice@quillanmail-<br>works.com</div>
    </div>
  </div>
  <div class="foot-brand">Quillan Mailworks</div>
  <div class="social" aria-label="Social links"><span></span><span></span><span></span></div>
</footer>

<div class="copyright">©<b>Quillan Mailworks Inc.</b> – 2016. All Rights Reserved</div>

</body>
</html>
```